Web Design for an Online Dating Web Site

We need an uncoded web design for a new online dating web site called zMatchy.net. Simplicity and boldness are the key factors in the successful design.
Please look at the requirements document attached for details.
Updates
Dear all,
Please AVOID USING A PICTURE OF A HAPPY COUPLE ON THE HOME PAGE of the site. We highly want to move away from this space as it makes our web site just like another dating web site.
We like something simple with web 2.0 look and feel. The examples in the Requirements Document are exactly the design we are after.
Regards
Tarn
Industry/Entity Type
Dating
Look and feel
Each slider illustrates characteristics of the customer's brand and the style your logo design should communicate.

```html
<!DOCTYPE html>
<html lang="en">
<head>
<meta charset="utf-8">
<title>zMatchy.net — Home</title>
<link href="https://fonts.googleapis.com/css2?family=Questrial&display=swap" rel="stylesheet">
<style>
:root{
  --page:#e9e6db;
  --page-light:#f4f2ea;
  --bar:#e1ded2;
  --pink:#e4337a;
  --pink-soft:#f06aa0;
  --grey:#8d8d8d;
  --nav:#6d8fae;
  --slider:#1c1c1c;
  --panel:#d9d6c9;
  --footer:#1d1d1d;
  --footer-text:#cfcfcf;
  --white:#ffffff;
  --blue:#6f96c2;
  --blue-dark:#3f6593;
}
*{box-sizing:border-box;margin:0;padding:0}
html,body{width:1200px;height:2204px;overflow:hidden}
body{position:relative;background:linear-gradient(var(--page-light),var(--page) 60%);font-family:"Questrial",sans-serif;color:var(--grey)}
.abs{position:absolute}

/* top bar */
.topbar{left:0;top:0;width:1200px;height:60px;background:var(--bar);border-bottom:1px solid #cfcbbd}
.field{height:36px;top:12px;background:var(--white);border:1px solid #bdb9ab;border-radius:4px;font-size:19px;color:#999;padding:6px 10px}
.login-btn{left:508px;top:12px;width:80px;height:36px;border:1px solid #bdb9ab;border-radius:4px;background:#eeece4;font-size:20px;text-align:center;line-height:34px;color:#888}
.or{left:628px;top:14px;font-size:24px;color:#aaa}
.share{top:14px;width:32px;height:32px;border-radius:4px;background:#c9c5b7}
.more{left:1034px;top:12px;font-size:28px;color:#aaa}

/* brand */
.brand{left:0;top:150px;width:1200px;text-align:center}
.brand-name{font-size:110px;color:var(--pink);letter-spacing:-2px;line-height:1}
.brand-dot{display:inline-block;width:22px;height:22px;border-radius:50%;background:var(--pink);margin-left:10px;vertical-align:top;margin-top:14px}
.brand-url{font-size:22px;color:var(--grey);margin-top:10px;margin-left:160px}

/* nav */
.nav{left:210px;top:318px;width:780px;height:56px;border-top:2px solid #cdc9bb;border-bottom:2px solid #cdc9bb;display:flex;justify-content:center;gap:46px;align-items:center}
.nav a{font-size:34px;color:var(--nav);text-decoration:none;letter-spacing:1px}

/* slider */
.slider{left:84px;top:470px;width:1032px;height:390px;background:linear-gradient(#2a2a2a,var(--slider));border-radius:18px;box-shadow:0 4px 16px rgba(0,0,0,.35)}
.slide-art{left:30px;top:20px;width:510px;height:360px;border-radius:10px;background:linear-gradient(135deg,#3a3a3a,#111 60%,#4a2136)}
.slide-title{left:580px;top:110px;font-size:44px;color:var(--white)}
.slide-sub{left:580px;top:165px;font-size:14px;color:#bbb;letter-spacing:1px;text-transform:uppercase}
.slide-body{left:580px;top:190px;width:400px;font-size:22px;line-height:1.3;color:#ddd}
.slide-btn{left:580px;top:265px;width:170px;height:56px;border-radius:6px;background:linear-gradient(#fafafa,#cfcfcf);color:#333;font-size:20px;text-align:center;line-height:56px;text-transform:uppercase}
.slide-note{left:580px;top:328px;font-size:12px;color:#999;text-transform:uppercase;letter-spacing:1px}
.arrow{top:636px;width:44px;height:56px;border-radius:6px;background:#c8d4e2}
.dots{left:560px;top:880px;display:flex;gap:8px}
.dots span{width:12px;height:12px;border-radius:50%;background:#bdb9ab}
.dots span:first-child{background:#777}

/* video */
.video{left:72px;top:970px;width:530px;height:370px;background:#cfccc0;border-radius:14px;padding:30px}
.video-thumb{width:100%;height:100%;background:linear-gradient(#fbfbfb,#e2e2e2);border-radius:4px;position:relative}
.play{position:absolute;left:205px;top:120px;width:70px;height:70px;border-radius:8px;background:#222}

/* sign up */
.signup{left:72px;top:1420px;width:530px;height:92px;border-radius:16px;background:linear-gradient(var(--blue),var(--blue-dark));color:var(--white);font-size:54px;line-height:92px;padding-left:44px;box-shadow:0 3px 8px rgba(0,0,0,.3)}

/* recent posts */
.posts{left:772px;top:975px;width:352px;height:540px;background:var(--panel);border-radius:14px;padding:30px 26px}
.posts h2{font-size:40px;font-weight:normal;color:#7d7d7d;margin-bottom:24px}
.post{display:flex;gap:14px;margin-bottom:34px}
.post-thumb{width:54px;height:54px;flex:none;background:linear-gradient(135deg,#8aa0b8,#5a6a4a)}
.post-title{font-size:23px;color:var(--pink);line-height:1.15}
.post-meta{font-size:11px;color:#999;margin-top:6px;text-transform:uppercase}

/* footer */
.footer{left:0;top:1615px;width:1200px;height:589px;background:var(--footer)}
.foot-brand{left:72px;top:85px;font-size:48px;color:var(--pink)}
.foot-brand span{display:inline-block;width:12px;height:12px;border-radius:50%;background:var(--pink);margin-left:6px;vertical-align:top;margin-top:8px}
.foot-col h3{font-size:40px;font-weight:normal;color:var(--white);margin-bottom:14px}
.foot-col a{display:block;font-size:22px;color:var(--footer-text);text-decoration:none;margin-bottom:12px}
.input{width:250px;height:32px;background:#3a3a3a;border:1px solid #555;font-size:18px;color:#999;padding:4px 10px;margin-bottom:10px}
.message{width:250px;height:156px;background:#2b2b2b;border:2px solid var(--pink-soft);margin-bottom:10px}
.post-btn{margin-left:150px;width:100px;height:30px;background:var(--pink-soft);color:var(--white);font-size:18px;text-align:center;line-height:30px}
.social{top:246px;width:80px;height:80px;border-radius:8px;background:#3c3c3c;border:2px solid #555}
.mini{top:342px;width:74px;height:26px;border-radius:4px;background:#e6e6e6;font-size:14px;color:#333;text-align:center;line-height:26px}
.mini.pink{background:var(--pink-soft);color:var(--white)}
</style>
</head>
<body>
<header class="abs topbar">
  <div class="abs field" style="left:70px;width:200px">username</div>
  <div class="abs field" style="left:290px;width:200px">password</div>
  <div class="abs login-btn">login</div>
  <div class="abs or">OR</div>
  <div class="abs share" style="left:670px"></div>
  <div class="abs share" style="left:714px"></div>
  <div class="abs share" style="left:758px"></div>
  <div class="abs share" style="left:802px"></div>
  <div class="abs share" style="left:846px"></div>
  <div class="abs share" style="left:890px"></div>
  <div class="abs more">more</div>
</header>

<div class="abs brand">
  <div class="brand-name">zMatchy<span class="brand-dot"></span></div>
  <div class="brand-url">zMatchy.net</div>
</div>

<nav class="abs nav">
  <a href="#">WHY</a><a href="#">HOW IT WORKS</a><a href="#">SIGN UP</a><a href="#">OUR BLOG</a>
</nav>

<section class="abs slider">
  <div class="abs slide-art" role="img" aria-label="Three smartphones showing the dating app screens"></div>
  <div class="abs slide-title">Great Mobile Apps</div>
  <div class="abs slide-sub">Some slogan goes here</div>
  <p class="abs slide-body">Lorem Ipsum is simply dummy text of the printing and typesetting industry.</p>
  <div class="abs slide-btn">Get Started</div>
  <div class="abs slide-note">Click only about our project</div>
</section>
<svg class="abs arrow" style="left:62px" viewBox="0 0 44 56"><path d="M28 14 14 28l14 14" fill="none" stroke="#4a6d94" stroke-width="6"/></svg>
<svg class="abs arrow" style="left:1094px" viewBox="0 0 44 56"><path d="M16 14l14 14-14 14" fill="none" stroke="#4a6d94" stroke-width="6"/></svg>
<div class="abs dots"><span></span><span></span><span></span><span></span><span></span></div>

<section class="abs video">
  <div class="video-thumb" role="img" aria-label="Animated video explaining why the site is different">
    <svg class="play" viewBox="0 0 70 70"><rect width="70" height="70" rx="8" fill="#222"/><path d="M26 18l26 17-26 17z" fill="#fff"/></svg>
  </div>
</section>

<div class="abs signup">Sign Up Today!</div>

<aside class="abs posts">
  <h2>Recent Posts</h2>
  <div class="post"><div class="post-thumb" role="img" aria-label="Blog post thumbnail"></div><div><div class="post-title">First Blog Post Title</div><div class="post-meta">Oct 6, 2011 · 0 comments · Read more</div></div></div>
  <div class="post"><div class="post-thumb" role="img" aria-label="Blog post thumbnail"></div><div><div class="post-title">Second Blog Post Title</div><div class="post-meta">Oct 6, 2011 · 0 comments · Read more</div></div></div>
  <div class="post"><div class="post-thumb" role="img" aria-label="Blog post thumbnail"></div><div><div class="post-title">Another Longer Blog Post Title</div><div class="post-meta">Oct 6, 2011 · 0 comments · Read more</div></div></div>
  <div class="post"><div class="post-thumb" role="img" aria-label="Blog post thumbnail"></div><div><div class="post-title">Final Post Title</div><div class="post-meta">Oct 6, 2011 · 0 comments · Read more</div></div></div>
</aside>

<footer class="abs footer">
  <div class="abs foot-brand">zMatchy<span></span></div>
  <div class="abs foot-col" style="left:72px;top:205px">
    <h3>Read More</h3>
    <a href="#">Why zMatchy</a><a href="#">How it Works</a><a href="#">Sign Up</a><a href="#">Login</a><a href="#">About Us</a>
  </div>
  <div class="abs foot-col" style="left:440px;top:205px">
    <h3>Let's Talk</h3>
    <div class="input">Name</div>
    <div class="input">Email</div>
    <div class="message"></div>
    <div class="post-btn">POST</div>
  </div>
  <div class="abs social" style="left:830px"></div>
  <div class="abs social" style="left:922px"></div>
  <div class="abs social" style="left:1014px"></div>
  <div class="abs mini" style="left:830px">Like</div>
  <div class="abs mini pink" style="left:914px">Share</div>
</footer>
</body>
</html>
```